Investment Real Estate Firm Needs Template to Showcase properties

We're a firm that sells $1M-$20M Dollar properties. We need a very professional template to be able to insert our information, pictures, and data into it. The data is mostly send via email in PDF and/or printed out. Here's the templates we need using OUR Logo and colors. Name of Company: Halden Capital Partners

1.)Cover Page Template: I've attached a example but we would like our own original cover page that looks cool and has spot for property photo
2.)Table of Contents Template: I've attached some cool original ideas that we like. Obviously would love our own
3.)Beginning of Section Template: Basically a page letting you know what section you're about ready to start.
4.) Content/Data Template: This is the template where all data will be inserted. So basically just bordering and very minimal space taken up to allow for content to be added
5.) Back Page/Last Page Template: This will be the last page of the presentation or showcase. I can also use this page to insert disclaimers and confidentiality language.

Target Market(s)

This only goes to a targeted personal client base

Industry/Entity Type

Real Estate

Font styles to use
Serif

Requirements
Must have
• - Cover Page, Contents Page, Section Page, Content Page, Back Page
• - Use our Logo. Attached
• - Use Our color scheme
• - Professional Look but some original ideas ;)
• - Abbility for me to edit and Drop in content
Nice to have
• Some Creativity in bordering and maybe carry over the section identity somehow within the border.
• A Extremely light but noticeable transparent "HCP" Logo Only on content pages in background centered " See attached

```html
<!DOCTYPE html>
<html lang="en">
<head>
<meta charset="utf-8">
<title>Halden Capital Partners — Cover Panel</title>
<link rel="stylesheet" href="https://fonts.googleapis.com/css2?family=Montserrat:wght@600&display=swap">
<style>
  :root {
    --panel-black: #000000;
    --gold-deep: #a8732a;
    --gold-mid: #c8963e;
    --gold-light: #f0c873;
    --silver-dark: #7d848c;
    --silver-mid: #c9d0d6;
    --silver-light: #f4f9fd;
    --stitch: #d9d9d9;
    --mark-grey: #4b4b4b;
  }
  html, body {
    margin: 0;
    padding: 0;
    width: 1200px;
    height: 900px;
    overflow: hidden;
    background: var(--panel-black);
  }
  .cover {
    position: relative;
    width: 1200px;
    height: 900px;
  }
  .cover-art {
    position: absolute;
    inset: 0;
    display: block;
  }
  .brand-initials {
    position: absolute;
    left: 0;
    top: 255px;
    width: 1200px;
    padding-left: 10px;
    text-align: center;
    font-family: "Montserrat", sans-serif;
    font-weight: 600;
    font-size: 300px;
    line-height: 1;
    letter-spacing: -12px;
    color: var(--mark-grey);
    margin: 0;
  }
</style>
</head>
<body>
  <main class="cover">
    <svg class="cover-art" width="1200" height="900" viewBox="0 0 1200 900" aria-hidden="true">
      <defs>
        <linearGradient id="gold-band" x1="0" y1="0" x2="1" y2="0">
          <stop offset="0" stop-color="var(--gold-deep)"/>
          <stop offset="0.3" stop-color="var(--gold-mid)"/>
          <stop offset="0.58" stop-color="var(--gold-light)"/>
          <stop offset="1" stop-color="var(--gold-deep)"/>
        </linearGradient>
        <linearGradient id="silver-band" x1="0" y1="0" x2="0" y2="1">
          <stop offset="0" stop-color="var(--silver-dark)"/>
          <stop offset="0.22" stop-color="var(--silver-mid)"/>
          <stop offset="0.5" stop-color="var(--silver-light)"/>
          <stop offset="0.72" stop-color="var(--silver-light)"/>
          <stop offset="1" stop-color="var(--silver-dark)"/>
        </linearGradient>
        <linearGradient id="silver-sheen" x1="0" y1="0" x2="1" y2="0">
          <stop offset="0" stop-color="#ffffff" stop-opacity="0.15"/>
          <stop offset="0.7" stop-color="#000000" stop-opacity="0"/>
          <stop offset="1" stop-color="#000000" stop-opacity="0.25"/>
        </linearGradient>
      </defs>

      <polygon class="silver-band" points="0,0 18,0 50,220 200,900 0,900" fill="url(#silver-band)"/>
      <polygon class="silver-sheen" points="0,0 18,0 50,220 200,900 0,900" fill="url(#silver-sheen)"/>

      <polygon class="gold-band" points="18,0 1200,0 1200,0 50,214" fill="url(#gold-band)"/>

      <polygon class="main-panel" points="50,222 1200,4 1200,900 200,900" fill="var(--panel-black)"/>

      <polyline class="stitch-line" points="1200,14 59,229 209,900"
        fill="none" stroke="var(--stitch)" stroke-width="1.5" stroke-dasharray="2 3"/>
    </svg>

    <p class="brand-initials">HCP</p>
  </main>
</body>
</html>
```